Electronic hardware design and manufacturer needing a new business card design.

We need a new business card design consisting of a double sided design adhering to brand and logo guidelines attached. I also want to incorporate something that recognizes our 25th year in business ("EST 2001" or something like that....).

Need extra days to review

Need extra days to review

```html
<!DOCTYPE html>
<html lang="en">
<head>
<meta charset="utf-8">
<title>Voltare Systems Corp. – Business Card</title>
<link href="https://fonts.googleapis.com/css2?family=Montserrat:wght@400;500;700&display=swap" rel="stylesheet">
<style>
  :root{
    --backdrop:#dedede;
    --navy:#062639;
    --navy-soft:#0c3147;
    --sky:#9bb8d8;
    --gold:#f7b733;
    --orange:#e07a33;
    --ink:#3a3a3a;
    --grey:#7a7a7a;
    --white:#ffffff;
    --band-1:#8e2023;
    --band-2:#dd532d;
    --band-3:#f58232;
    --band-4:#fbb934;
  }
  *{margin:0;padding:0;box-sizing:border-box}
  html,body{width:1200px;height:1200px;overflow:hidden;background:var(--backdrop);font-family:"Montserrat",sans-serif}
  .card{position:absolute;left:180px;width:867px;height:498px;overflow:hidden}
  .card--front{top:85px;background:var(--navy)}
  .card--back{top:626px;background:var(--white)}

  .brand-band{position:absolute;left:0;right:0;bottom:0;display:flex}
  .card--front .brand-band{height:23px}
  .card--back .brand-band{height:18px}
  .brand-band span{flex:1}
  .brand-band span:nth-child(1){background:var(--band-1)}
  .brand-band span:nth-child(2){background:var(--band-2)}
  .brand-band span:nth-child(3){background:var(--band-3)}
  .brand-band span:nth-child(4){background:var(--band-4)}

  .established{position:absolute;left:36px;top:33px;font-size:30px;font-weight:700;letter-spacing:2px;color:var(--sky)}
  .established .est{color:var(--gold)}

  .texture{position:absolute;right:20px;top:0;width:360px;height:475px;
    background:radial-gradient(ellipse at 70% 45%, var(--navy-soft) 0%, rgba(12,49,71,0) 70%)}

  .wordmark{position:absolute;display:flex;align-items:center;gap:14px;font-weight:700;white-space:nowrap}
  .wordmark .mark{display:block;flex:none}
  .card--front .wordmark{left:253px;top:225px;font-size:30px;color:var(--sky)}
  .card--front .wordmark .mark{width:22px;height:22px;background:var(--band-3)}
  .card--back .wordmark{left:86px;top:206px;width:320px;font-size:28px;line-height:1.2;color:var(--navy)}
  .card--back .wordmark .mark{width:22px;height:22px;background:var(--band-3)}

  .divider{position:absolute;left:434px;top:123px;width:2px;height:274px;background:#b8b8b8}
  .divider::before{content:"";position:absolute;left:0;top:0;width:2px;height:54px;background:var(--orange)}

  .contact{position:absolute;left:456px;top:112px}
  .contact .name{font-size:32px;font-weight:700;color:var(--orange);letter-spacing:.5px;line-height:1.1}
  .contact .title{font-size:26px;font-weight:400;color:var(--grey);letter-spacing:1px;line-height:1.1;margin-top:2px}
  .contact address{font-style:normal;font-size:21px;font-weight:500;color:var(--ink);letter-spacing:1.4px;line-height:34px;margin-top:20px}
  .contact ul{list-style:none;margin-top:20px}
  .contact li{display:flex;align-items:center;height:38px;font-size:21px;font-weight:500;color:var(--ink);letter-spacing:1.4px}
  .contact li svg{width:24px;height:24px;margin-right:16px;flex:none}
</style>
</head>
<body>

<section class="card card--front" aria-label="Card front">
  <div class="texture" role="img" aria-label="Faint scattered square texture"></div>
  <p class="established"><span class="est">EST.</span> 2001</p>
  <div class="wordmark"><span class="mark"></span>VOLTARE SYSTEMS CORP.</div>
  <div class="brand-band"><span></span><span></span><span></span><span></span></div>
</section>

<section class="card card--back" aria-label="Card back">
  <div class="wordmark"><span class="mark"></span><span>VOLTARE SYSTEMS<br>CORP.</span></div>
  <div class="divider"></div>
  <div class="contact">
    <h1 class="name">DANIEL MORROW</h1>
    <p class="title">President</p>
    <address>1840 Ridgeview Road NE, Unit 7<br>Lakeport, Alberta T4K 1R8</address>
    <ul>
      <li>
        <svg viewBox="0 0 24 24" fill="none" stroke="#e07a33" stroke-width="2" stroke-linecap="round" stroke-linejoin="round"><path d="M5 3h4l2 5-3 2a11 11 0 0 0 6 6l2-3 5 2v4a2 2 0 0 1-2 2A17 17 0 0 1 3 5a2 2 0 0 1 2-2z"/></svg>
        (403) 555-0142
      </li>
      <li>
        <svg viewBox="0 0 24 24" fill="none" stroke="#e07a33" stroke-width="2" stroke-linejoin="round"><rect x="2" y="5" width="20" height="14"/><path d="M2 5l10 8 10-8M2 19l7-7M22 19l-7-7"/></svg>
        hello@voltaresystems.ca
      </li>
      <li>
        <svg viewBox="0 0 24 24" fill="none" stroke="#e07a33" stroke-width="2"><circle cx="12" cy="12" r="10"/><ellipse cx="12" cy="12" rx="4" ry="10"/><path d="M2 12h20M4 7h16M4 17h16"/></svg>
        voltaresystems.ca
      </li>
    </ul>
  </div>
  <div class="brand-band"><span></span><span></span><span></span><span></span></div>
</section>

</body>
</html>
```